Candy Packaging

I'm looking for a logo design for a confectionary company called Gran's Sweet Delights.
Something that will be appealing to women.
The packaging in interested in will be a stand up guseted bag with a window.
Dimensions ar 7 1/2in high, 4in wide 2in thick.

Im trying to upload pictures of the product and I'm not sure if the're loading.

Target Market(s)

Adult Females

Industry/Entity Type

It Company

```html
<!DOCTYPE html>
<html lang="en">
<head>
<meta charset="utf-8">
<title>Gran's Sweet Delights – Colored Balls Bag Front</title>
<link rel="stylesheet" href="https://fonts.googleapis.com/css2?family=Oswald:wght@500;600&family=Lobster&display=swap">
<style>
  :root {
    --bag-black: #141414;
    --band-grey: #4a4a4a;
    --band-light: #6a6a6a;
    --brand-green: #3fb23b;
    --script-yellow: #f3e28c;
    --claim-yellow: #efe3a0;
    --burst-red: #d2123f;
    --white: #f4f4f4;
    --candy-pink: #e0457f;
    --candy-orange: #f28a2e;
    --candy-yellow: #f2e23a;
    --candy-green: #2fb24f;
  }
  html, body {
    margin: 0;
    padding: 0;
    overflow: hidden;
  }
  body {
    width: 1041px;
    height: 1200px;
    background: var(--bag-black);
  }
  .bag-front {
    position: relative;
    width: 1041px;
    height: 1200px;
    overflow: hidden;
    background: var(--bag-black);
  }
  .artwork {
    position: absolute;
    inset: 0;
  }
  .brand-name {
    position: absolute;
    left: 157px;
    top: 210px;
    width: 560px;
    margin: 0;
    text-align: center;
    font-family: "Oswald", sans-serif;
    font-weight: 600;
    font-size: 78px;
    line-height: 1.05;
    letter-spacing: 2px;
    color: var(--brand-green);
    text-transform: uppercase;
  }
  .taste-badge {
    position: absolute;
    left: 797px;
    top: 267px;
    width: 220px;
    height: 220px;
  }
  .taste-badge-text {
    position: absolute;
    inset: 0;
    display: flex;
    align-items: center;
    justify-content: center;
    text-align: center;
    font-family: "Oswald", sans-serif;
    font-weight: 500;
    font-size: 32px;
    line-height: 1.05;
    color: var(--white);
    transform: rotate(-4deg);
  }
  .product-name {
    position: absolute;
    left: 80px;
    top: 470px;
    width: 640px;
    margin: 0;
    text-align: center;
    font-family: "Lobster", cursive;
    font-weight: 400;
    font-size: 92px;
    color: var(--script-yellow);
    transform: rotate(-13deg);
  }
  .claims {
    position: absolute;
    left: 70px;
    top: 1040px;
    margin: 0;
    padding: 0;
    list-style: none;
    font-family: "Oswald", sans-serif;
    font-weight: 500;
    font-size: 27px;
    line-height: 36px;
    color: var(--claim-yellow);
    text-transform: uppercase;
  }
  .claims li::before {
    content: "\2605";
    margin-right: 14px;
  }
  .net-weight {
    position: absolute;
    right: 66px;
    top: 1058px;
    margin: 0;
    font-family: "Oswald", sans-serif;
    font-weight: 600;
    font-size: 36px;
    color: var(--white);
  }
</style>
</head>
<body>
<main class="bag-front">
  <svg class="artwork" viewBox="0 0 1041 1200" width="1041" height="1200" aria-hidden="false">
    <defs>
      <linearGradient id="bandGradient" x1="0" y1="0" x2="1" y2="0">
        <stop offset="0" stop-color="var(--band-grey)"/>
        <stop offset="0.5" stop-color="var(--band-light)"/>
        <stop offset="1" stop-color="var(--band-grey)"/>
      </linearGradient>
      <linearGradient id="candyGradient" x1="0" y1="0" x2="1" y2="1">
        <stop offset="0" stop-color="var(--candy-orange)"/>
        <stop offset="0.35" stop-color="var(--candy-pink)"/>
        <stop offset="0.6" stop-color="var(--candy-yellow)"/>
        <stop offset="0.8" stop-color="var(--candy-green)"/>
        <stop offset="1" stop-color="var(--candy-orange)"/>
      </linearGradient>
    </defs>

    <!-- upper sweep band -->
    <path class="sweep-band" d="M0 700 C 250 640, 620 560, 1041 520" fill="none" stroke="url(#bandGradient)" stroke-width="22"/>
    <!-- lower sweep band -->
    <path class="sweep-band" d="M0 905 C 300 960, 700 1000, 1041 1020" fill="none" stroke="url(#bandGradient)" stroke-width="22"/>

    <!-- window ring -->
    <path class="window-ring" d="M40 800 C 40 630, 700 545, 950 565 C 1050 575, 1050 770, 995 870 C 910 975, 500 1015, 190 975 C 60 955, 40 880, 40 800 Z" fill="none" stroke="var(--band-grey)" stroke-width="26"/>

    <!-- product window -->
    <path class="product-window" role="img" aria-label="Photo of colourful sugar-coated candy balls in pink, orange, yellow and green" d="M60 800 C 60 645, 700 565, 945 585 C 1030 595, 1030 765, 980 860 C 900 955, 500 995, 200 955 C 80 937, 60 875, 60 800 Z" fill="url(#candyGradient)"/>
  </svg>

  <h1 class="brand-name">Gran's<br>Sweet Delights</h1>

  <div class="taste-badge">
    <svg viewBox="0 0 220 220" width="220" height="220" aria-hidden="true">
      <polygon fill="var(--burst-red)" points="110,5 126,48 160,15 160,62 205,45 180,86 215,110 180,134 205,175 160,158 160,205 126,172 110,215 94,172 60,205 60,158 15,175 40,134 5,110 40,86 15,45 60,62 60,15 94,48"/>
    </svg>
    <p class="taste-badge-text">TASTE<br>LIKE<br>HOME</p>
  </div>

  <h2 class="product-name">Colored Balls</h2>

  <ul class="claims">
    <li>Less Sugar</li>
    <li>No Artificial Taste</li>
    <li>No Additives</li>
  </ul>

  <p class="net-weight">500g</p>
</main>
</body>
</html>
```